Brightwire Hollow Business cards

one side I would like my logo (uploaded) and the other side I want my details. I'm an electrician in sydney. The logo side I'm happy with just a white background and our logo in the middle.

Details for other side
24/7 Sydney Electrician
Marcus Pell
0431 587 219
marcus@brightwirehollow.com.au
brightwirehollow.com.au
icons for facebook, instagram, linked in

Industry/Entity Type

electrician

Contact Information for Business Card

company info

```html
<!DOCTYPE html>
<html lang="en">
<head>
<meta charset="utf-8">
<title>Brightwire Hollow – Business Cards</title>
<link href="https://fonts.googleapis.com/css2?family=Montserrat:wght@600;700&display=swap" rel="stylesheet">
<style>
  :root {
    --backdrop: #b3b3b3;
    --card: #ffffff;
    --accent: #d9261c;
    --ink: #111111;
    --cord: #b5b5b5;
  }
  * { margin: 0; padding: 0; box-sizing: border-box; }
  html, body { width: 1200px; height: 1200px; overflow: hidden; }
  body {
    background: var(--backdrop);
    font-family: "Montserrat", Arial, sans-serif;
    position: relative;
  }
  .card {
    position: absolute;
    left: 243px;
    width: 714px;
    height: 462px;
    background: var(--card);
    overflow: hidden;
    box-shadow: 0 10px 28px rgba(0,0,0,0.28);
  }
  .card--front { top: 86px; }
  .card--back { top: 651px; }

  .decor { position: absolute; inset: 0; }

  .brand-name {
    position: absolute;
    left: 0; right: 0;
    top: 210px;
    text-align: center;
    font-weight: 700;
    font-size: 34px;
    letter-spacing: 0.02em;
    color: var(--accent);
  }

  .holder {
    position: absolute;
    left: 0; right: 0;
    top: 38px;
    text-align: center;
  }
  .holder__name {
    display: inline-block;
    font-weight: 700;
    font-size: 27px;
    letter-spacing: 0.01em;
    color: var(--ink);
    padding-bottom: 6px;
    border-bottom: 5px solid var(--accent);
    border-radius: 0 0 3px 3px;
    line-height: 1.2;
  }

  .contact {
    position: absolute;
    left: 0; right: 0;
    text-align: center;
  }
  .contact__icon { display: block; margin: 0 auto; width: 19px; height: 19px; }
  .contact__text {
    display: block;
    margin-top: 5px;
    font-weight: 700;
    font-size: 20px;
    line-height: 1.2;
    color: var(--ink);
    letter-spacing: 0.02em;
  }
  .contact--phone { top: 121px; }
  .contact--email { top: 191px; }
  .contact--web { top: 256px; }

  .socials {
    position: absolute;
    left: 0; right: 0;
    top: 339px;
    display: flex;
    justify-content: center;
    gap: 19px;
  }
  .socials__dot {
    width: 20px; height: 20px;
    border-radius: 50%;
    background: var(--accent);
  }

  .tagline {
    position: absolute;
    left: 0; right: 0;
    top: 394px;
    display: flex;
    justify-content: center;
    align-items: center;
    gap: 20px;
  }
  .tagline__text {
    font-weight: 700;
    font-size: 17px;
    letter-spacing: 0.2em;
    color: var(--ink);
  }
  .tagline__dot {
    width: 22px; height: 22px;
    border-radius: 50%;
    background: var(--accent);
  }
</style>
</head>
<body>

<section class="card card--front">
  <svg class="decor" width="714" height="462" viewBox="0 0 714 462" aria-hidden="true">
    <line x1="-5" y1="64" x2="538" y2="64" stroke="var(--cord)" stroke-width="9" stroke-linecap="round"/>
    <circle cx="630" cy="67" r="66" fill="var(--cord)"/>
    <line x1="178" y1="398" x2="720" y2="398" stroke="var(--cord)" stroke-width="9" stroke-linecap="round"/>
    <circle cx="83" cy="395" r="66" fill="var(--cord)"/>
  </svg>
  <h1 class="brand-name">Brightwire Hollow</h1>
</section>

<section class="card card--back">
  <div class="holder"><h2 class="holder__name">MARCUS PELL</h2></div>

  <div class="contact contact--phone">
    <svg class="contact__icon" viewBox="0 0 20 20" aria-hidden="true">
      <circle cx="10" cy="10" r="10" fill="var(--accent)"/>
      <path d="M6.3 5.2c.4-.4 1-.3 1.3.1l1 1.5c.3.4.2.9-.1 1.2l-.6.5c.5 1.2 1.4 2.1 2.6 2.6l.5-.6c.3-.3.8-.4 1.2-.1l1.5 1c.4.3.5.9.1 1.3l-.7.8c-.5.5-1.3.6-2 .3-2.4-1-4.3-2.9-5.3-5.3-.3-.7-.2-1.5.3-2z" fill="#fff"/>
    </svg>
    <span class="contact__text">0431 587 219</span>
  </div>

  <div class="contact contact--email">
    <svg class="contact__icon" viewBox="0 0 20 20" aria-hidden="true">
      <circle cx="10" cy="10" r="10" fill="var(--accent)"/>
      <rect x="4.5" y="6.5" width="11" height="7.5" rx="0.8" fill="none" stroke="#fff" stroke-width="1.2"/>
      <path d="M4.8 7l5.2 4 5.2-4M4.8 13.6l3.8-3.2M15.2 13.6l-3.8-3.2" fill="none" stroke="#fff" stroke-width="1.1"/>
    </svg>
    <span class="contact__text">marcus@brightwirehollow.com.au</span>
  </div>

  <div class="contact contact--web">
    <svg class="contact__icon" viewBox="0 0 20 20" aria-hidden="true">
      <circle cx="10" cy="10" r="10" fill="var(--accent)"/>
      <circle cx="10" cy="10" r="5.5" fill="none" stroke="#fff" stroke-width="1.2"/>
      <ellipse cx="10" cy="10" rx="2.4" ry="5.5" fill="none" stroke="#fff" stroke-width="1.1"/>
      <path d="M4.5 10h11" stroke="#fff" stroke-width="1.1"/>
    </svg>
    <span class="contact__text">brightwirehollow.com.au</span>
  </div>

  <div class="socials">
    <span class="socials__dot" role="img" aria-label="Social profile one"></span>
    <span class="socials__dot" role="img" aria-label="Social profile two"></span>
    <span class="socials__dot" role="img" aria-label="Social profile three"></span>
  </div>

  <div class="tagline">
    <span class="tagline__dot" aria-hidden="true"></span>
    <span class="tagline__text">24/7 SYDNEY ELECTRICIAN</span>
    <span class="tagline__dot" aria-hidden="true"></span>
  </div>
</section>

</body>
</html>
```